Zielgruppe
Zeitarbeit Personalvermittlung Arbeitsvermittlung Arbeitnehmerüberlassung
Zielgruppe:
Akademiker
Fachkräfte
Politiker
Ingenieur
wichtige Akteure der Gesellschaft
Kommunen
Vereinigungen
Aufgabenstellung
Wir benötigen schlichte und dezente, aber eindrucksvolle,exklusive Visitenkarten mit unserem Logo.
Aufbau:
Vorname, Name
Position
Telefon
Mobil
E-Mail
Fax
Unsere Website: http://www.velmaris-personal.de
Wir sind 2 Geschäftsführer also bitte für beide Namen
Dies benötigen wir als PSD, PDF, JPG, sodass wir selbst die Angaben nach Belieben eintragen können.

```html
<!DOCTYPE html>
<html lang="de">
<head>
<meta charset="utf-8">
<title>Velmaris Visitenkarten</title>
<link rel="stylesheet" href="https://fonts.googleapis.com/css2?family=Arimo:wght@400&display=swap">
<style>
  :root {
    --page: #e9e9ea;
    --card-light: #ffffff;
    --card-dark: #33373a;
    --ink: #2b2d2f;
    --ink-soft: #55585b;
    --accent: #ee7216;
    --on-dark: #ffffff;
    --on-dark-soft: #c9cbcd;
  }
  * { margin: 0; padding: 0; box-sizing: border-box; }
  html, body { width: 1200px; height: 873px; overflow: hidden; background: var(--page); }
  body {
    font-family: "Arimo", Arial, sans-serif;
    display: flex; align-items: center; justify-content: center; gap: 60px;
  }
  .card {
    width: 520px; height: 336px; position: relative;
    box-shadow: 0 10px 28px rgba(0,0,0,.18);
  }
  .card--front { background: var(--card-light); color: var(--ink); }
  .card--back {
    background: radial-gradient(circle at 55% 45%, #4a4e52 0%, var(--card-dark) 60%);
    color: var(--on-dark);
    display: flex; align-items: center; justify-content: center;
  }
  .brand { display: flex; align-items: center; gap: 12px; }
  .brand__dot { width: 22px; height: 22px; border-radius: 50%; background: var(--accent); }
  .brand__name { font-size: 54px; line-height: 1; letter-spacing: 1px; }
  .brand__tag { font-size: 10px; letter-spacing: 5.2px; margin-top: 8px; padding-left: 36px; }
  .card--front .brand__name { color: var(--ink); }
  .card--front .brand__tag { color: var(--ink-soft); }
  .card--back .brand__name { color: var(--on-dark); font-size: 62px; }
  .card--back .brand__tag { color: var(--on-dark-soft); letter-spacing: 6px; }

  .front__logo { position: absolute; top: 30px; left: 34px; }
  .person { position: absolute; top: 142px; left: 34px; font-size: 14px; line-height: 1.35; }
  .person__name { font-size: 17px; }
  .person__role { color: var(--accent); font-size: 13px; margin-bottom: 6px; }
  .contact {
    position: absolute; top: 188px; right: 30px;
    font-size: 13.5px; line-height: 1.4; text-align: right;
  }
  .contact__label { color: var(--accent); margin-right: 4px; }
  .web { position: absolute; bottom: 34px; left: 34px; color: var(--accent); font-size: 20px; }
  .strip { position: absolute; left: 0; right: 0; bottom: 0; height: 14px; background: var(--card-dark); }
</style>
</head>
<body>
  <section class="card card--front" aria-label="Visitenkarte Vorderseite">
    <div class="front__logo">
      <div class="brand"><span class="brand__dot"></span><span class="brand__name">velmaris</span></div>
      <div class="brand__tag">PERSONALDIENSTLEISTUNGEN GMBH</div>
    </div>
    <div class="person">
      <div class="person__name">Lukas Wendler</div>
      <div class="person__role">Geschäftsführer</div>
      <div>Lindenweg 14</div>
      <div>62318 Auenstadt</div>
    </div>
    <div class="contact">
      <div><span class="contact__label">T</span>02361 - 48 57 10</div>
      <div><span class="contact__label">M</span>0157 - 36 91 42 07</div>
      <div>info@velmaris-personal.de</div>
      <div><span class="contact__label">F</span>02361 - 48 57 19</div>
    </div>
    <div class="web">www.velmaris-personal.de</div>
    <div class="strip"></div>
  </section>

  <section class="card card--back" aria-label="Visitenkarte Rückseite">
    <div class="back__logo">
      <div class="brand"><span class="brand__dot"></span><span class="brand__name">velmaris</span></div>
      <div class="brand__tag">PERSONALDIENSTLEISTUNGEN</div>
    </div>
  </section>
</body>
</html>
```